Assessment Report cover design and formatting

This report is for senior executives and provides leaders with detailed insight into their capabilities and skills. The cover should have space for the date and name of the person doing the assessment. We are looking to modernise the report cover design. We would like the report to be our company colours if possible. The work will likely expand once the cover is done to other parts of the report, ie. the format and layout of the report etc.

Company colours:
Primary colours:
• Blue #0D47A1, #115CD0, #90B6ED, #EEf3FB
• Green #0D91A1, #47A10D, #324C196, #0DA11D
Additional colours:
• Purple #A10D91
• Brown #A1670D
• Red #A10D47

Target Market(s)

Executives

Industry/Entity Type

Consulting, leadership development

Colors
0094D4
00A9DD
6FCCEA
C7EBF8
E9F6FB
00AB8E
00BBA5
67D7C9
C6EFE9
E9F9F6
E54698
E96AAD
F1A4CE
F9D9EA
FCEFF6
6B429C
8869AF
B7A5CE
E3DAEB
F3F0F8

Requirements
Must have
• The report cover should have space for name of user, the date and company logo. Cover should be in A4 size.

```html
<!DOCTYPE html>
<html lang="en">
<head>
<meta charset="utf-8">
<title>Growth Leader Assessment – Insight Report</title>
<link rel="stylesheet" href="https://fonts.googleapis.com/css2?family=Saira+Extra+Condensed:wght@500;600&family=Saira+Condensed:wght@800&family=Montserrat:wght@600;800;900&display=swap">
<style>
  :root {
    --navy: #0D47A1;
    --blue: #115CD0;
    --sky: #90B6ED;
    --mist: #EEF3FB;
    --green: #0DA11D;
    --lime: #47C21A;
    --teal: #0D91A1;
    --white: #FFFFFF;
  }
  html, body {
    margin: 0;
    padding: 0;
    width: 848px;
    height: 1200px;
    overflow: hidden;
    background: var(--white);
  }
  .cover {
    position: relative;
    width: 848px;
    height: 1200px;
    overflow: hidden;
  }
  .cover-art {
    position: absolute;
    inset: 0;
    width: 848px;
    height: 1200px;
  }
  .display-condensed {
    font-family: "Saira Extra Condensed", "Arial Narrow", sans-serif;
  }
  .display-heavy {
    font-family: "Montserrat", Arial, sans-serif;
  }
  .title-growth { font-weight: 600; font-size: 145px; }
  .title-leader { font-weight: 900; font-size: 106px; }
  .title-assessment { font-weight: 500; font-size: 100px; }
  .report-label-text { font-weight: 500; font-size: 50px; }
  .report-month { font-weight: 800; font-size: 46px; }
  .report-year {
    font-family: "Saira Condensed", "Arial Narrow", sans-serif;
    font-weight: 800;
    font-size: 165px;
  }
  .brand-name { font-weight: 600; font-size: 34px; }
</style>
</head>
<body>
<main class="cover">
  <svg class="cover-art" viewBox="0 0 848 1200" xmlns="http://www.w3.org/2000/svg">
    <defs>
      <linearGradient id="office-tone" x1="0" y1="0" x2="1" y2="1">
        <stop offset="0" stop-color="#222a36"/>
        <stop offset="0.5" stop-color="#3c4656"/>
        <stop offset="1" stop-color="#5a6474"/>
      </linearGradient>
      <linearGradient id="abstract-tone" x1="0" y1="0" x2="0.4" y2="1">
        <stop offset="0" stop-color="#2f5fa8"/>
        <stop offset="0.45" stop-color="#2c4c86"/>
        <stop offset="1" stop-color="#3a3f52"/>
      </linearGradient>
      <linearGradient id="sweep-band" x1="0" y1="0" x2="1" y2="0">
        <stop offset="0" stop-color="#12a32a"/>
        <stop offset="0.45" stop-color="#0a8f7e"/>
        <stop offset="1" stop-color="#0a6db7"/>
      </linearGradient>
      <linearGradient id="corner-band" x1="0" y1="1" x2="1" y2="0">
        <stop offset="0" stop-color="#12a32a"/>
        <stop offset="0.5" stop-color="#0a8f86"/>
        <stop offset="1" stop-color="#0b5fcc"/>
      </linearGradient>
      <linearGradient id="growth-fill" gradientUnits="userSpaceOnUse" x1="0" y1="143" x2="0" y2="246">
        <stop offset="0" stop-color="#eef3fb"/>
        <stop offset="0.45" stop-color="#eef3fb"/>
        <stop offset="1" stop-color="#115CD0"/>
      </linearGradient>
      <linearGradient id="label-fill" x1="0" y1="0" x2="1" y2="0">
        <stop offset="0" stop-color="#139a2a"/>
        <stop offset="0.4" stop-color="#1d7f48"/>
        <stop offset="1" stop-color="#143c50" stop-opacity="0.35"/>
      </linearGradient>
      <linearGradient id="year-fill" gradientUnits="userSpaceOnUse" x1="0" y1="822" x2="0" y2="938">
        <stop offset="0" stop-color="#12a32a"/>
        <stop offset="1" stop-color="#0b5fcc"/>
      </linearGradient>
    </defs>

    <rect class="photo-office" x="0" y="0" width="848" height="1200" fill="url(#office-tone)" role="img" aria-label="Photo of colleagues talking in a bright office meeting"/>

    <path class="sweep-white" d="M0 0 H848 V640 C650 730 250 720 0 428 Z" fill="#ffffff"/>
    <path class="sweep-band" d="M0 0 H848 V628 C640 695 270 668 0 362 Z" fill="url(#sweep-band)"/>
    <path class="photo-abstract" d="M0 0 H848 V624 C610 680 230 600 0 245 Z" fill="url(#abstract-tone)" role="img" aria-label="Abstract blue architectural backdrop"/>

    <path class="corner-stripe" d="M290 1200 C350 985 560 812 848 805 V1200 Z" fill="#eef3fb"/>
    <path class="corner-band" d="M318 1200 C385 995 590 826 848 808 V1200 Z" fill="url(#corner-band)"/>
    <path class="corner-panel" d="M364 1200 C440 1010 630 840 848 812 V1200 Z" fill="#ffffff"/>

    <g class="title" role="heading" aria-level="1">
      <text class="display-condensed title-growth" x="395" y="245" textLength="365" lengthAdjust="spacingAndGlyphs" fill="url(#growth-fill)">GROWTH</text>
      <text class="display-heavy title-leader" x="398" y="340" textLength="370" lengthAdjust="spacingAndGlyphs" fill="#ffffff" stroke="#0D91A1" stroke-width="4" paint-order="stroke fill">LEADER</text>
      <text class="display-condensed title-assessment" x="394" y="432" textLength="362" lengthAdjust="spacingAndGlyphs" fill="#ffffff">ASSESSMENT</text>
    </g>

    <g class="report-label">
      <rect x="89" y="741" width="340" height="70" fill="url(#label-fill)"/>
      <text class="display-condensed report-label-text" x="106" y="792" textLength="280" lengthAdjust="spacingAndGlyphs" fill="#ffffff">INSIGHT REPORT FOR</text>
    </g>

    <g class="report-date">
      <text class="display-heavy report-month" transform="translate(134 938) rotate(-90)" textLength="100" lengthAdjust="spacingAndGlyphs" fill="#3fcf1a">AUG</text>
      <text class="report-year" x="148" y="936" textLength="242" lengthAdjust="spacingAndGlyphs" fill="url(#year-fill)" stroke="#ffffff" stroke-width="5" paint-order="stroke fill">2023</text>
    </g>

    <text class="display-heavy brand-name" x="656" y="1060" text-anchor="middle" textLength="270" lengthAdjust="spacingAndGlyphs" fill="#0D47A1">Meridian Advisory</text>
  </svg>
</main>
</body>
</html>
```